Business Card Design Project

2 sided business card utilizing existing logo
- English on one side, Arabic on the other side (both English and Arabic text will be provided)
Same color scheme as logo
Information included will be: name, title, email, phone, address and website (www.dravelnix.com)
Updates

Target Market(s)

We are a Systems Integration Company

Industry/Entity Type

Business

Font styles to use
Serif
Sans Serif

Requirements
Should not have
• We prefer using the flat logo rather than one with shadow/3D effect

```html
<!DOCTYPE html>
<html lang="en">
<head>
<meta charset="utf-8">
<title>Dravelnix Business Card</title>
<link rel="stylesheet" href="https://fonts.googleapis.com/css2?family=Didact+Gothic&display=swap">
<style>
  :root {
    --brand-red: #ec1c2a;
    --ink-grey: #5b5b5d;
    --card-white: #ffffff;
  }
  * { margin: 0; padding: 0; box-sizing: border-box; }
  html, body {
    width: 1200px;
    height: 816px;
    overflow: hidden;
    background: var(--card-white);
  }
  .card {
    position: relative;
    width: 1200px;
    height: 816px;
    background: var(--card-white);
    font-family: "Didact Gothic", sans-serif;
    color: var(--ink-grey);
    overflow: hidden;
  }
  .accent-stripe {
    position: absolute;
    inset: 0;
    width: 1200px;
    height: 816px;
  }
  .brand-name {
    position: absolute;
    left: 40px;
    width: 540px;
    top: 366px;
    text-align: center;
    font-size: 60px;
    letter-spacing: 10px;
    color: var(--brand-red);
    line-height: 1;
  }
  .contact-block {
    position: absolute;
    right: 60px;
    top: 60px;
    text-align: right;
  }
  .person-name {
    font-size: 41px;
    color: var(--brand-red);
    line-height: 1.2;
  }
  .person-title {
    font-size: 31px;
    line-height: 1.5;
    margin-top: 6px;
  }
  .contact-line {
    font-size: 31px;
    line-height: 1.5;
    display: flex;
    justify-content: flex-end;
    align-items: center;
    gap: 12px;
  }
  .contact-icon {
    width: 26px;
    height: 26px;
    fill: var(--brand-red);
  }
  .address-block {
    position: absolute;
    right: 60px;
    bottom: 70px;
    text-align: right;
  }
  .address-line {
    font-size: 31px;
    line-height: 1.6;
  }
  .website {
    font-size: 35px;
    line-height: 1.7;
    letter-spacing: 1px;
  }
  .website .domain { color: var(--brand-red); }
</style>
</head>
<body>
  <div class="card">
    <svg class="accent-stripe" viewBox="0 0 1200 816" aria-hidden="true">
      <path d="M300 -12 L562 300 Q612 370 560 436 L218 830"
            fill="none" stroke="var(--brand-red)" stroke-width="18" stroke-linejoin="round"/>
    </svg>

    <div class="brand-name">DRAVELNIX</div>

    <div class="contact-block">
      <div class="person-name">Name Here</div>
      <div class="person-title">Title Here</div>
      <div class="contact-line">
        <span>name@dravelnix.com</span>
        <svg class="contact-icon" viewBox="0 0 24 24" aria-hidden="true">
          <path d="M2 6h20v2l-10 6L2 8z M2 10l10 6 10-6v9H2z"/>
        </svg>
      </div>
      <div class="contact-line">
        <span>(000) 123-4567</span>
        <svg class="contact-icon" viewBox="0 0 24 24" aria-hidden="true">
          <path d="M7 1h10a2 2 0 0 1 2 2v18a2 2 0 0 1-2 2H7a2 2 0 0 1-2-2V3a2 2 0 0 1 2-2zm0 3v13h10V4zm5 15a1.3 1.3 0 1 0 0 2.6A1.3 1.3 0 0 0 12 19z"/>
        </svg>
      </div>
    </div>

    <div class="address-block">
      <div class="address-line">address line 1</div>
      <div class="address-line">address line 2</div>
      <div class="website">www.<span class="domain">dravelnix</span>.com</div>
    </div>
  </div>
</body>
</html>
```